Business Card Design - Nubrova

Who we are?
Nubrova.com is a new social media platform setup for use by all businesses looking to grow social engagement with their brands, products and services.

What are we after?
We need creative business cards designed which will also feature a new company logo.
After a few attempts to develop business cards internally we felt we didn't achieve the results we were after - see the attached files below.

Our Design Parameters:
Essentially the business card needs to feature a new Nubrova logo.
- The logo needs to have the first letter of Nubrova 'N' within an Tulvo type tile/box.
- The other letters of Nubrova 'ubrova' can be in a specific font that resembles our site look and feel
- We attempted to make the card black and white - see the attached files but other warmer colours may also work - please don't use the wooded background that's featured on the website
- The website is about social integration and sharing of media - it would be great if that could come through in the design of the business cards
- Overall feel - tulvo type look
- Logo must be on one side of the card as per the attached files

- The business card needs to feature our slogal - "Social Media Marketing"
- The business card needs to have credit card dimensions

Refer to www.nubrova-example.com for an overview of the company

Please return the completed business card in PSD format.

Hi All,
Thanks for all the great designs.

I have added additional files with variations of the logos. We prefer for the N to be embossed within a white tile as it appears in the attachments.

Couple of pointers:
As I indicated black/black or black/white front and back would work best for us.

Black front with the logo in white as it appears in the attached files and white back with the logo on one side and contact details etc on the other.
The side with the contact details needs to appear elegant and modern, the logo on the other side can be a bit warmer and playful.

Also what I think would work well on the logo side of the business card is the N blended into the background - almost in the form of a watermark as it appears in the attached file - Logo Sample.pptx (but more subtle).

Pleaes refer to the other files for examples of what we are aiming for.

Thank you all.

Cheers,
Nubrova

• Refer to the attached file for formatting of the business card - logo in full size on one side and Name, title, address, contact details on the other

```html
<!DOCTYPE html>
<html lang="en">
<head>
<meta charset="utf-8">
<title>Nubrova Business Cards</title>
<link rel="stylesheet" href="https://fonts.googleapis.com/css2?family=Open+Sans:wght@400;700&family=Arimo:wght@700&display=swap">
<style>
  :root {
    --page: #ece7e1;
    --card-top: #3e3e3e;
    --card-mid: #2c2c2c;
    --card-edge: #1c1c1c;
    --logo: #d9d9d9;
    --text: #f2f2f2;
    --rule: #8a8a8a;
  }
  * { margin: 0; padding: 0; box-sizing: border-box; }
  html, body { width: 1200px; height: 1096px; overflow: hidden; }
  body { background: var(--page); position: relative; font-family: "Open Sans", sans-serif; }

  .card {
    position: absolute;
    border-radius: 22px;
    background: radial-gradient(ellipse at 50% 35%, var(--card-top) 0%, var(--card-mid) 55%, var(--card-edge) 100%);
    overflow: hidden;
  }
  .card--details { left: 40px; top: 57px; width: 787px; height: 448px; }
  .card--logo { left: 322px; top: 562px; width: 786px; height: 448px; }

  .wordmark {
    position: absolute;
    font-family: "Open Sans", sans-serif;
    font-weight: 700;
    color: var(--logo);
    letter-spacing: -1px;
    line-height: 1;
    white-space: nowrap;
  }
  .card--details .wordmark { left: 38px; top: 190px; font-size: 76px; }
  .card--logo .wordmark { left: 0; right: 0; top: 146px; text-align: center; font-size: 112px; }

  .divider {
    position: absolute; left: 450px; top: 96px;
    width: 1px; height: 264px; background: var(--rule);
  }

  .contact { position: absolute; left: 467px; top: 103px; color: var(--text); }
  .contact__name { font-weight: 700; font-size: 20px; line-height: 27px; padding-left: 4px; }
  .contact__title { font-size: 18px; line-height: 27px; }
  .contact__address { font-size: 18px; line-height: 27px; margin-top: 17px; }
  .contact__list { list-style: none; margin-top: 17px; font-size: 18px; line-height: 27.5px; }
  .contact__list li { display: flex; align-items: center; gap: 7px; }
  .contact__list svg { width: 14px; height: 14px; fill: var(--text); flex: none; }

  .slogan {
    position: absolute; left: 0; right: 0; top: 326px;
    text-align: center; color: var(--text);
    font-family: "Arimo", sans-serif; font-weight: 700; font-size: 40px;
    letter-spacing: 0.5px;
  }
</style>
</head>
<body>

<section class="card card--details" aria-label="Card side with contact details">
  <div class="wordmark">NUBROVA</div>
  <div class="divider"></div>
  <div class="contact">
    <p class="contact__name">Dorian Vesk</p>
    <p class="contact__title">Business Development Manager</p>
    <p class="contact__address">41-45 Larkfield Street<br>East Brinmoor 3187</p>
    <ul class="contact__list">
      <li>
        <svg viewBox="0 0 14 14" aria-hidden="true"><rect x="3" y="0" width="8" height="14" rx="1.5"/><rect x="4.5" y="2" width="5" height="5" fill="#333"/></svg>
        0400 555 318
      </li>
      <li>
        <svg viewBox="0 0 14 14" aria-hidden="true"><path d="M3 1l3 3-1.5 2c1 2 2 3 3.5 3.5L10 8l3 3-2 2C6 13 1 8 1 3z"/></svg>
        1300 555 462
      </li>
      <li>
        <svg viewBox="0 0 14 14" aria-hidden="true"><rect x="1" y="3.5" width="12" height="8"/><path d="M1 3.5l6 4.5 6-4.5" stroke="#333" stroke-width="1.2" fill="none"/></svg>
        dorian@nubrova-example.com
      </li>
      <li>
        <svg viewBox="0 0 14 14" aria-hidden="true"><circle cx="7" cy="7" r="6"/><path d="M1 7h12M7 1v12M3 3.5q4 2 8 0M3 10.5q4-2 8 0" stroke="#333" stroke-width="1" fill="none"/></svg>
        www.nubrova-example.com
      </li>
    </ul>
  </div>
</section>

<section class="card card--logo" aria-label="Card side with name and slogan">
  <div class="wordmark">NUBROVA</div>
  <p class="slogan">Social Media Marketing</p>
</section>

</body>
</html>
```